브랜드 소개
다온먹거리나눔진흥원는 『농수산식품산업 진흥을 통해 국민의 안정적인 먹거리 확보와 삶의질 향상에 기여』를 목표로 설립되어 유통개선·수급안정·수출진흥·식품산업육성 등의 사업을 수행하고 있습니다. 홈페이지는 공사 홍보 및 각종 공고 안내, 공사의 다양한 지원사업에 대한 창구 역할을 하고 있습니다. 다온먹거리나눔진흥원의 타겟은 농어업인과 소비자입니다.

```html
<!DOCTYPE html>
<html lang="ko">
<head>
<meta charset="utf-8">
<title>다온먹거리나눔진흥원 소개</title>
<link rel="stylesheet" href="https://fonts.googleapis.com/css2?family=Noto+Sans+KR:wght@300;400;500;700&display=swap">
<style>
  :root {
    --sky-blue: #6f9dc6;
    --sky-pale: #e9eff3;
    --field-tone: #b7c08a;
    --teal: #1d6b7a;
    --icon-blue: #2e9cc4;
    --icon-light: #7cc6df;
    --text-dark: #2f3336;
    --chevron: #b9d3e2;
  }
  html, body {
    margin: 0;
    padding: 0;
    width: 1200px;
    height: 1200px;
    overflow: hidden;
  }
  body {
    font-family: "Noto Sans KR", sans-serif;
    color: var(--text-dark);
  }
  .canvas {
    position: relative;
    width: 1200px;
    height: 1200px;
    overflow: hidden;
  }
  .landscape-photo {
    position: absolute;
    inset: 0;
    background: linear-gradient(180deg, var(--sky-blue) 0%, var(--sky-pale) 45%, var(--sky-pale) 75%, var(--field-tone) 100%);
  }
  .headline {
    position: absolute;
    top: 300px;
    left: 0;
    width: 1200px;
    margin: 0;
    text-align: center;
    font-weight: 300;
    font-size: 38px;
    letter-spacing: -0.5px;
    color: var(--text-dark);
    white-space: nowrap;
  }
  .headline .key {
    display: inline-block;
    font-size: 74px;
    font-weight: 400;
    color: var(--teal);
    margin: 0 14px;
    vertical-align: -8px;
    letter-spacing: 4px;
  }
  .headline .key span {
    position: relative;
    display: inline-block;
  }
  .headline .key span::before {
    content: "";
    position: absolute;
    top: -14px;
    left: 50%;
    width: 5px;
    height: 5px;
    margin-left: -2.5px;
    border-radius: 50%;
    background: var(--teal);
  }
  .services {
    position: absolute;
    top: 455px;
    left: 0;
    width: 1200px;
    height: 150px;
  }
  .service {
    position: absolute;
    top: 0;
    width: 240px;
    margin-left: -120px;
    text-align: center;
  }
  .service svg { display: block; margin: 0 auto; }
  .service-label {
    margin-top: 22px;
    font-size: 25px;
    font-weight: 700;
    color: var(--text-dark);
  }
  .chevron { position: absolute; top: 30px; }
  .mission {
    position: absolute;
    top: 640px;
    left: 0;
    width: 1200px;
    text-align: center;
    font-size: 24px;
    font-weight: 500;
    line-height: 52px;
    letter-spacing: -0.5px;
    color: var(--text-dark);
  }
  .mission p { margin: 0; }
</style>
</head>
<body>
<div class="canvas">
  <div class="landscape-photo" role="img" aria-label="구름이 떠 있는 푸른 하늘과 그 아래 펼쳐진 초록빛·황금빛 들판 풍경 사진"></div>

  <h1 class="headline">대한민국 <span class="key"><span>농</span><span>수</span><span>산</span><span>식</span><span>품</span></span>의 행복한 변화가 시작됩니다!</h1>

  <div class="services">
    <div class="service" style="left:176px">
      <svg width="80" height="90" viewBox="0 0 80 90" aria-hidden="true">
        <rect x="14" y="10" width="52" height="72" rx="4" fill="none" stroke="var(--icon-blue)" stroke-width="4"/>
        <rect x="28" y="4" width="24" height="12" rx="3" fill="var(--icon-blue)"/>
        <line x1="24" y1="30" x2="56" y2="30" stroke="var(--icon-light)" stroke-width="4"/>
        <line x1="24" y1="42" x2="56" y2="42" stroke="var(--icon-light)" stroke-width="4"/>
        <polyline points="26,60 35,69 54,52" fill="none" stroke="var(--icon-blue)" stroke-width="4"/>
      </svg>
      <div class="service-label">유통개선</div>
    </div>
    <svg class="chevron" style="left:302px" width="28" height="44" viewBox="0 0 28 44" aria-hidden="true"><polyline points="6,4 22,22 6,40" fill="none" stroke="var(--chevron)" stroke-width="5"/></svg>

    <div class="service" style="left:456px">
      <svg width="90" height="90" viewBox="0 0 90 90" aria-hidden="true">
        <path d="M30 10 A18 18 0 1 0 46 20" fill="none" stroke="var(--icon-blue)" stroke-width="7"/>
        <rect x="28" y="64" width="8" height="18" fill="var(--icon-light)"/>
        <rect x="42" y="54" width="8" height="28" fill="var(--icon-blue)"/>
        <rect x="56" y="44" width="8" height="38" fill="var(--icon-blue)"/>
        <rect x="70" y="34" width="8" height="48" fill="var(--icon-blue)"/>
      </svg>
      <div class="service-label">수급안정</div>
    </div>
    <svg class="chevron" style="left:576px" width="28" height="44" viewBox="0 0 28 44" aria-hidden="true"><polyline points="6,4 22,22 6,40" fill="none" stroke="var(--chevron)" stroke-width="5"/></svg>

    <div class="service" style="left:744px">
      <svg width="120" height="90" viewBox="0 0 120 90" aria-hidden="true">
        <path d="M8 56 L20 52 L34 60 L92 32 C102 27 112 30 108 36 C104 42 96 44 88 48 L44 70 L30 72 Z" fill="none" stroke="var(--icon-blue)" stroke-width="4" stroke-linejoin="round"/>
        <path d="M56 46 L40 28 L50 26 L74 40" fill="none" stroke="var(--icon-blue)" stroke-width="4" stroke-linejoin="round"/>
        <line x1="20" y1="82" x2="70" y2="82" stroke="var(--icon-light)" stroke-width="4"/>
        <line x1="40" y1="74" x2="60" y2="74" stroke="var(--icon-light)" stroke-width="3"/>
      </svg>
      <div class="service-label">수출진흥</div>
    </div>
    <svg class="chevron" style="left:866px" width="28" height="44" viewBox="0 0 28 44" aria-hidden="true"><polyline points="6,4 22,22 6,40" fill="none" stroke="var(--chevron)" stroke-width="5"/></svg>

    <div class="service" style="left:1006px">
      <svg width="100" height="90" viewBox="0 0 100 90" aria-hidden="true">
        <rect x="6" y="14" width="24" height="34" rx="3" transform="rotate(-40 18 31)" fill="none" stroke="var(--icon-blue)" stroke-width="4"/>
        <rect x="70" y="14" width="24" height="34" rx="3" transform="rotate(40 82 31)" fill="none" stroke="var(--icon-blue)" stroke-width="4"/>
        <path d="M28 46 L50 68 C54 72 60 72 64 66 L76 50" fill="none" stroke="var(--icon-blue)" stroke-width="4" stroke-linejoin="round"/>
        <path d="M72 44 L56 30 C52 26 46 28 42 32 L36 38" fill="none" stroke="var(--icon-light)" stroke-width="4" stroke-linejoin="round"/>
      </svg>
      <div class="service-label">식품산업 육성</div>
    </div>
  </div>

  <div class="mission">
    <p>국민 모두가 믿고 먹을 수 있는 건강하고 안전한 농수산식품!</p>
    <p>dN가 농업인의 터전에서 농업인과 함께 그 희망을 만들어갑니다.</p>
    <p>농업인과 소비자 모두가 행복한 창조농업, dN가 새롭게 시작합니다.</p>
  </div>
</div>
</body>
</html>
```